July 15 Raffle Fundraiser to raise $2000

Fundraiser for the family to travel to Halifax NB and support athlete Corvel Ashbury.
Travel dates: July 16-23,2023

Raffling off three prizes
1) $150.00 Firewood
2) $375.00 Red Safe
3) $300.00 Secure Latch and door knob
4) 20 pieces of frozen coho sockeye

Tickets are
$2.00 each
$5.00 for three

Draw Date: July 15,2023 @11:00am

Please help us raise $2000.00
To alleviate travelling and meal costs
ETransfer: ashburyfundraiser482@plimvex.com

I have included the pervious flyer we used
Information on there as well
And please try keep same Color scheme

Thanks

Target Market(s)

Athlete supporters

Colors

Designer to choose colors to be used in the design.

Requirements
Must have
• Pictures of the raffle items , with exception of the fish there no picture of fish
Nice to have
• Pictures of the athlete in a minimal way. Similar to the colours and design of previous flyer to stay consistent. But fine if it is different.

```html
<!DOCTYPE html>
<html lang="en">
<head>
<meta charset="utf-8">
<title>Raffle Fundraiser Flyer</title>
<link rel="stylesheet" href="https://fonts.googleapis.com/css2?family=Anton&family=Poppins:wght@500;600;700;800&family=Teko:wght@500;600;700&display=swap">
<style>
:root{
  --yellow:#e9c419;
  --blue:#0f5bb8;
  --blue-deep:#0a3f8f;
  --ink:#111418;
  --gray:#55585c;
  --line:#9aa0a6;
  --paper:#ffffff;
  --bg:#c9cacd;
}
*{box-sizing:border-box;margin:0;padding:0}
html,body{width:1200px;height:1076px;overflow:hidden;background:var(--bg)}
body{display:flex;align-items:center;justify-content:center;font-family:"Poppins",sans-serif;color:var(--ink)}
.flyer{position:relative;width:800px;height:1036px;background:var(--paper);overflow:hidden;box-shadow:0 10px 30px rgba(0,0,0,.18)}
.abs{position:absolute;white-space:nowrap}

/* headline */
.title{left:50px;top:40px;font-family:"Anton",sans-serif;font-size:88px;line-height:1;color:var(--yellow);letter-spacing:1px;-webkit-text-stroke:2px var(--ink)}
.subtitle{left:58px;top:140px;font-family:"Teko",sans-serif;font-weight:600;font-size:34px;line-height:1;letter-spacing:1px}
.destination{left:110px;top:178px;width:355px;height:58px;background:var(--blue);font-family:"Teko",sans-serif;font-weight:700;font-size:46px;line-height:64px;color:var(--yellow);letter-spacing:9px;padding-left:10px}
.pin{left:64px;top:182px;width:46px;height:50px;background:var(--yellow);border-radius:8px;display:flex;align-items:center;justify-content:center}
.support{left:82px;top:254px;font-weight:700;font-size:15px}
.athlete{left:80px;top:272px;font-weight:700;font-size:44px;line-height:1.2;color:var(--blue);letter-spacing:-.5px}
.dates{left:80px;top:342px;width:380px;height:100px;background:var(--yellow);border-radius:0 18px 18px 18px}
.dates-tail{left:50px;top:430px;width:80px;height:10px;background:var(--yellow);border-radius:6px}
.dates-label{left:104px;top:360px;font-family:"Anton",sans-serif;font-size:34px;line-height:1}
.dates-label span{display:block;font-family:"Poppins",sans-serif;font-weight:500;font-size:24px;letter-spacing:7px;margin-top:4px}
.month{left:262px;top:358px;width:30px;height:70px;background:#fff;font-family:"Teko",sans-serif;font-weight:700;font-size:26px;color:var(--blue);writing-mode:vertical-rl;transform:rotate(180deg);text-align:center;line-height:30px}
.days{left:298px;top:348px;font-family:"Teko",sans-serif;font-weight:700;font-size:48px;line-height:1;color:var(--blue)}
.days sup{font-size:20px;vertical-align:22px}
.year{left:306px;top:400px;width:98px;height:30px;border:2px solid var(--ink);font-family:"Teko",sans-serif;font-weight:700;font-size:28px;line-height:30px;text-align:center;letter-spacing:4px}

/* photo */
.photo-frame{left:470px;top:-10px;width:340px;height:430px;border:4px solid var(--blue);border-radius:0 0 0 28px;background:#fff;padding:6px}
.photo{width:100%;height:100%;border-radius:0 0 0 22px;background:linear-gradient(160deg,#1d5fc4 0%,#0b3c93 55%,#0a2f72 100%)}

/* raffle box */
.raffle{left:330px;top:468px;width:450px;height:244px;border:4px solid var(--blue);border-radius:18px;background:#fff}
.raffle-head{left:340px;top:478px;width:430px;height:44px;background:var(--yellow);border-radius:10px 10px 0 0;font-weight:700;font-size:18px;text-align:center;line-height:44px;letter-spacing:.5px}
.bow{left:528px;top:452px}
.prizes{left:344px;top:530px;width:422px;height:130px;display:flex}
.prize{flex:1;position:relative;text-align:center;border-right:2px solid #d7dade}
.prize:last-child{border-right:0}
.badge{position:relative;margin:16px auto 0;width:96px;height:52px;background:var(--gray);border-radius:48px 48px 0 0;color:#fff;font-family:"Teko",sans-serif;font-weight:600;font-size:26px;line-height:60px;outline:2px solid var(--gray);outline-offset:3px}
.num{position:absolute;top:-14px;left:50%;margin-left:-13px;width:26px;height:26px;border-radius:50%;background:var(--blue);border:2px solid #fff;color:#fff;font-family:"Poppins",sans-serif;font-size:13px;font-weight:600;line-height:22px;text-align:center}
.prize-name{margin-top:12px;font-weight:700;font-size:15px;line-height:1.15}
.fish{left:358px;top:662px;width:394px;height:32px;background:var(--blue);color:#fff;font-weight:600;font-size:16px;text-align:center;line-height:30px;border:2px solid var(--ink)}

/* prize photos */
.gallery{left:60px;top:480px;width:240px;height:280px;background:#d6d8db;border:3px solid var(--gray);border-radius:22px;padding:10px;display:flex;flex-direction:column;gap:8px}
.shot{flex:1;border-radius:14px;position:relative}
.shot.wood{background:linear-gradient(135deg,#8a5a3c,#5b3a26)}
.shot.safe{background:linear-gradient(135deg,#b3202a,#3b3b3f)}
.shot.lock{background:linear-gradient(135deg,#c9c7c0,#a07a4e)}
.shot .num{top:16px;left:auto;right:-24px;margin:0}

/* draw date */
.draw{left:372px;top:752px;width:400px;height:82px;border:1.5px solid var(--line);border-radius:24px}
.draw-label{left:400px;top:738px;background:#fff;padding:0 8px;font-weight:700;font-size:19px;color:var(--blue)}
.draw-when{left:394px;top:778px;display:flex;align-items:center;gap:8px;font-weight:700;font-size:24px}

/* tickets */
.tickets{left:70px;top:782px;width:260px;height:172px;border:1.5px solid var(--line);border-radius:22px}
.tickets-label{left:110px;top:768px;background:#fff;padding:0 8px;font-weight:700;font-size:19px}
.ticket{left:92px;width:220px;height:64px;display:flex;flex-direction:column;justify-content:center;padding-left:24px;border-right:2px dashed rgba(255,255,255,.7)}
.ticket b{font-weight:700;font-size:32px;line-height:1}
.ticket small{font-family:"Teko",sans-serif;font-weight:600;font-size:20px;line-height:1}
.t-each{top:808px;background:var(--yellow);color:var(--ink)}
.t-three{top:878px;background:var(--blue);color:#fff}

/* goal */
.goal-band{left:420px;top:858px;width:350px;height:46px;background:var(--yellow);font-weight:800;font-size:27px;line-height:46px;text-align:center;color:var(--ink)}
.goal{left:420px;top:902px;width:350px;font-weight:800;font-size:66px;line-height:1;color:var(--blue);letter-spacing:-1px;text-align:center}
.costs{left:380px;top:982px;width:420px;height:30px;background:var(--gray);color:#fff;font-weight:500;font-size:15px;line-height:30px;padding-left:150px;display:flex;gap:6px;align-items:center}
.alleviate{left:360px;top:982px;width:150px;height:30px;background:var(--blue);color:#fff;font-family:"Teko",sans-serif;font-weight:600;font-size:22px;line-height:32px;text-align:center;clip-path:polygon(10% 0,100% 0,100% 100%,0 100%)}
.etransfer{left:380px;top:1013px;font-weight:600;font-size:15px}
.etransfer a{color:var(--blue);text-decoration:none}

/* partners */
.team{left:70px;top:990px;display:flex;align-items:center;gap:6px;font-weight:700;font-size:15px;color:var(--blue)}
.team i{display:block;width:12px;height:12px;border-radius:50%;background:var(--blue)}
.games{left:252px;top:966px;width:60px;height:60px;border:2px solid var(--ink);background:#eaf2fb}
</style>
</head>
<body>
<main class="flyer">
  <div class="abs photo-frame"><div class="photo" role="img" aria-label="Photo of the athlete cheering on a basketball court, tinted blue"></div></div>

  <h1 class="abs title">FUNDRAISER</h1>
  <p class="abs subtitle">FOR THE FAMILY TO TRAVEL TO</p>
  <div class="abs pin">
    <svg width="24" height="32" viewBox="0 0 24 32"><path d="M12 0C5.4 0 0 5.3 0 11.8 0 20.6 12 32 12 32s12-11.4 12-20.2C24 5.3 18.6 0 12 0z" fill="#fff"/><circle cx="12" cy="12" r="4.5" fill="#e9c419"/></svg>
  </div>
  <p class="abs destination">HALIFAX NB</p>
  <p class="abs support">AND SUPPORT ATHLETE</p>
  <h2 class="abs athlete">Corvel Ashbury</h2>

  <div class="abs dates"></div>
  <div class="abs dates-tail"></div>
  <p class="abs dates-label">TRAVEL<span>DATES</span></p>
  <p class="abs month">JULY</p>
  <p class="abs days">16<sup>TH</sup>–23<sup>RD</sup></p>
  <p class="abs year">2023</p>

  <svg class="abs bow" width="70" height="24" viewBox="0 0 70 24"><path d="M35 20 L8 4 L14 20 Z M35 20 L62 4 L56 20 Z" fill="#0f5bb8"/><rect x="0" y="18" width="70" height="5" fill="#0f5bb8"/></svg>
  <div class="abs raffle"></div>
  <h3 class="abs raffle-head">RAFFLING OFF THREE PRIZES</h3>
  <div class="abs prizes">
    <div class="prize"><div class="badge"><span class="num">1</span>$150.00</div><p class="prize-name">Firewood</p></div>
    <div class="prize"><div class="badge"><span class="num">2</span>$375.00</div><p class="prize-name">Red Safe</p></div>
    <div class="prize"><div class="badge"><span class="num">3</span>$300.00</div><p class="prize-name">Secure Latch<br>&amp; door knob</p></div>
  </div>
  <p class="abs fish">20 PIECES OF FROZEN COHO SOCKEYE</p>

  <div class="abs gallery">
    <div class="shot wood" role="img" aria-label="Photo of a stack of firewood"><span class="num">1</span></div>
    <div class="shot safe" role="img" aria-label="Photo of the red safe"><span class="num">2</span></div>
    <div class="shot lock" role="img" aria-label="Photo of the keypad latch and door knob"><span class="num">3</span></div>
  </div>

  <div class="abs draw"></div>
  <p class="abs draw-label">DRAW DATES</p>
  <div class="abs draw-when">
    <svg width="28" height="26" viewBox="0 0 30 28"><rect x="1" y="4" width="28" height="23" rx="3" fill="#fff" stroke="#e9c419" stroke-width="2"/><rect x="1" y="4" width="28" height="7" fill="#e9c419"/><g fill="#e9c419"><rect x="6" y="14" width="4" height="4"/><rect x="13" y="14" width="4" height="4"/><rect x="20" y="14" width="4" height="4"/><rect x="6" y="20" width="4" height="4"/><rect x="13" y="20" width="4" height="4"/></g></svg>
    <span>JULY 15,2023</span>
    <svg width="26" height="26" viewBox="0 0 28 28"><circle cx="14" cy="14" r="12" fill="#e9c419"/><circle cx="14" cy="14" r="8.5" fill="#fff"/><path d="M14 9v5l4 3" stroke="#111418" stroke-width="2" fill="none"/></svg>
    <span>11:00AM</span>
  </div>

  <div class="abs tickets"></div>
  <p class="abs tickets-label">TICKETS ARE</p>
  <div class="abs ticket t-each"><b>$2.00</b><small>Each</small></div>
  <div class="abs ticket t-three"><b>$5.00</b><small>For Three</small></div>

  <p class="abs goal-band">PLEASE HELP US RAISE</p>
  <p class="abs goal">$2000.00</p>
  <div class="abs costs">
    <svg width="16" height="16" viewBox="0 0 16 16"><circle cx="8" cy="8" r="7" fill="#e9c419"/></svg>
    <span>TRAVELLING &amp;</span>
    <svg width="16" height="16" viewBox="0 0 16 16"><circle cx="8" cy="8" r="7" fill="#e9c419"/></svg>
    <span>MEAL COSTS</span>
  </div>
  <p class="abs alleviate">TO ALLEVIATE</p>
  <p class="abs etransfer">ETransfer: <a href="mailto:ashburyfundraiser482@plimvex.com">ashburyfundraiser482@plimvex.com</a></p>

  <p class="abs team"><i></i>Team Coastline</p>
  <div class="abs games" role="img" aria-label="Partner games badge"></div>
</main>
</body>
</html>
```